Health care technology software systems

We have a solid logo. We have company colors that will need to be used as well. We just need a great business card design. We sell to health plans but want to be modern
Updates

Need extra days to review

Target Market(s)

Health technology sector selling into Health Plans

Industry/Entity Type

Health Care Technology

Contact Information for Business Card

Name, title, address, phone number, email

Requirements
Must have
• Use of Kembrata corporate colors - Uploaded w/ our logos

```html
<!DOCTYPE html>
<html lang="en">
<head>
<meta charset="utf-8">
<title>Kembrata Business Card</title>
<link rel="stylesheet" href="https://fonts.googleapis.com/css2?family=Montserrat:wght@300;400;800&display=swap">
<style>
  :root {
    --page-bg: #141414;
    --card-bg: #2a2a2a;
    --ink-white: #ffffff;
    --brand-green: #8cc63f;
    --brand-blue: #1ba6e0;
    --brand-indigo: #3d5fb8;
  }
  * { box-sizing: border-box; margin: 0; padding: 0; }
  html, body {
    width: 1200px; height: 900px; overflow: hidden;
    background: var(--page-bg);
    font-family: "Montserrat", Arial, sans-serif;
    color: var(--ink-white);
  }
  .sheet { position: relative; width: 1200px; height: 900px; }
  .card {
    position: absolute; left: 270px; width: 660px; height: 377px;
    background: var(--card-bg); border-radius: 16px;
    box-shadow: 0 10px 30px rgba(0,0,0,.55);
  }
  .card--front { top: 48px; }
  .card--back { top: 475px; }

  .wordmark {
    display: flex; align-items: center;
  }
  .wordmark__dot {
    border-radius: 50%; background: var(--brand-blue); flex: none;
  }
  .wordmark__name { font-weight: 300; color: var(--ink-white); letter-spacing: 1px; }

  .card--front .wordmark {
    position: absolute; left: 0; right: 0; top: 0; bottom: 0; justify-content: center; gap: 26px;
  }
  .card--front .wordmark__dot { width: 68px; height: 68px; }
  .card--front .wordmark__name { font-size: 86px; line-height: 1; }

  .card--back .wordmark { position: absolute; left: 40px; top: 112px; gap: 14px; }
  .card--back .wordmark__dot { width: 34px; height: 34px; }
  .card--back .wordmark__name { font-size: 46px; line-height: 1; }

  .person { position: absolute; right: 40px; top: 38px; text-align: right; }
  .person__name { font-weight: 800; font-size: 22px; letter-spacing: 1.5px; text-transform: uppercase; }
  .person__first { color: var(--brand-green); }
  .person__last { color: var(--brand-blue); }
  .person__title { font-size: 14px; margin-top: 2px; }

  .contact { position: absolute; left: 40px; bottom: 34px; font-size: 16px; line-height: 1.45; }
  .contact__address { margin-bottom: 10px; }
  .contact__list { list-style: none; }
  .contact__item { display: flex; align-items: center; gap: 10px; }
  .contact__icon { width: 16px; height: 16px; fill: var(--brand-green); flex: none; }
</style>
</head>
<body>
<main class="sheet">
  <section class="card card--front" aria-label="Card front">
    <div class="wordmark">
      <span class="wordmark__dot"></span>
      <span class="wordmark__name">kembrata</span>
    </div>
  </section>

  <section class="card card--back" aria-label="Card back">
    <div class="person">
      <p class="person__name"><span class="person__first">Delwin</span> <span class="person__last">Harrow</span></p>
      <p class="person__title">Owner/CEO</p>
    </div>

    <div class="wordmark">
      <span class="wordmark__dot"></span>
      <span class="wordmark__name">kembrata</span>
    </div>

    <div class="contact">
      <p class="contact__address">418 Corvel Avenue AB<br>Marrow County Name 7702</p>
      <ul class="contact__list">
        <li class="contact__item">
          <svg class="contact__icon" viewBox="0 0 16 16"><path d="M1 6c0-2 3-4 7-4s7 2 7 4v1h-3V5.5C10.5 5 9.3 4.8 8 4.8S5.5 5 4 5.5V7H1z"/><path d="M4 8h8l2 6H2z"/></svg>
          <span>123-608-37514</span>
        </li>
        <li class="contact__item">
          <svg class="contact__icon" viewBox="0 0 16 16"><path d="M1 3h14v1.2L8 9 1 4.2z"/><path d="M1 6l7 4.8L15 6v7H1z"/></svg>
          <span>info@companyname.com</span>
        </li>
        <li class="contact__item">
          <svg class="contact__icon" viewBox="0 0 16 16"><circle cx="8" cy="8" r="7" fill="none" stroke="var(--brand-green)" stroke-width="1.6"/><path d="M1.5 8h13M8 1c2.2 2 2.2 12 0 14M8 1c-2.2 2-2.2 12 0 14" fill="none" stroke="var(--brand-green)" stroke-width="1.3"/></svg>
          <span>www.companyname.com</span>
        </li>
      </ul>
    </div>
  </section>
</main>
</body>
</html>
```